Bespoke Builders Business Card Design

We need a business card for an established builder of high quality bespoke homes in Auckland and Northland. We build and renovate homes collaboratively facilitating effective communication between owners, builders, architects, suppliers and tradespeople. We have never built or renovated a home that leaks or has faults. We only use reliable materials. We have never been sued or had legal action taken against us. We are honest builders of bespoke homes not group mass produced homes. Our niche market is in character homes. We practice sustainability and have built a lot of coastal property. We have been in business for over thirty years . We would like to see natural colors of the environment sand,sea and maybe vegetation . The design should communicate quality, sustainability,fair pricing, open communication and the originality of bespoke building. And the fact that the builder is registered.

Business

Rowan Tillery Builders
Ph. 027318592
18 Garnet Rd Ferndale Bay Auckland 0814
PO Box 958 Mangawhai 0371

```html
<!DOCTYPE html>
<html lang="en">
<head>
<meta charset="utf-8">
<title>Rowan Tillery Builders – Business Card</title>
<link rel="stylesheet" href="https://fonts.googleapis.com/css2?family=EB+Garamond:wght@500&family=Open+Sans:wght@400&display=swap">
<style>
  :root {
    --page-bg: #ecebe8;
    --card-bg: #ffffff;
    --ink: #111111;
    --earth-brown: #6e2e14;
    --sand-yellow: #d9c824;
    --contact-text: #ffffff;
  }
  * { margin: 0; padding: 0; box-sizing: border-box; }
  html, body {
    width: 1189px;
    height: 1200px;
    overflow: hidden;
    background: var(--page-bg);
  }
  .sheet {
    position: relative;
    width: 1189px;
    height: 1200px;
  }
  .card {
    position: absolute;
    left: 136px;
    width: 917px;
    height: 522px;
    background: var(--card-bg);
    border: 1px solid #d6d4cf;
    overflow: hidden;
  }
  .card--front { top: 46px; }
  .card--back { top: 623px; }

  .business-name {
    font-family: "EB Garamond", "Palatino Linotype", serif;
    font-weight: 500;
    font-size: 66px;
    color: var(--ink);
    white-space: nowrap;
    line-height: 1;
  }

  .title-row {
    position: absolute;
    top: 118px;
    left: 0;
    right: 0;
    display: flex;
    align-items: center;
    gap: 14px;
  }
  .title-rule {
    flex: 1;
    height: 2px;
    background: var(--ink);
  }

  .earth-band {
    position: absolute;
    left: 0;
    top: 0;
    width: 917px;
    height: 522px;
  }
  .earth-band__base { fill: var(--earth-brown); }
  .earth-band__stripe { fill: var(--sand-yellow); }

  .contact {
    position: absolute;
    left: 0;
    right: 0;
    top: 352px;
    text-align: center;
    font-family: "Open Sans", "Segoe UI", sans-serif;
    font-size: 25px;
    line-height: 37px;
    color: var(--contact-text);
    list-style: none;
  }

  .card--back .business-name {
    position: absolute;
    top: 50%;
    left: 0;
    right: 0;
    text-align: center;
    transform: translateY(-50%);
  }
</style>
</head>
<body>
<main class="sheet">
  <section class="card card--front" aria-label="Card front">
    <svg class="earth-band" viewBox="0 0 917 522" aria-hidden="true">
      <path class="earth-band__base" d="M0 338 Q458 216 917 338 L917 522 L0 522 Z"/>
      <path class="earth-band__stripe" d="M0 348 Q458 258 917 348 L917 369 Q458 245 0 369 Z"/>
    </svg>
    <div class="title-row">
      <span class="title-rule"></span>
      <h1 class="business-name">Rowan Tillery Builders</h1>
      <span class="title-rule"></span>
    </div>
    <ul class="contact">
      <li class="contact__phone">027318592</li>
      <li class="contact__street">18 Garnet Rd Ferndale Bay Auckland 0814</li>
      <li class="contact__postal">PO Box 958 Mangawhai 0371</li>
    </ul>
  </section>

  <section class="card card--back" aria-label="Card back">
    <p class="business-name">Rowan Tillery Builders</p>
  </section>
</main>
</body>
</html>
```